Business Card Design

We need a new business card for our restaurant/motel as we are new owners. Our business is in a small community in a rainforest north of Townsville, Queensland AUSTRALIA and we are on a mountain 3000 feet above sea level. Visitors come here to see the wide variety of birds (This area is especially noted for the cassowary and riflebird), travel the many bush walks and enjoy the cooler climate. We would like you to use as the main colours blue and green - the buildings are painted in those colours and reflect the green for the forest and blue for the rain/sky. Yellow could also be used. The card should be bright and cheerful.
Travel
Ferncrest Lodge Yarrondi
Licensed Café/ Restaurant & Motel
14 Coralwood Lane KELBRIDGE Qld 4823
Ph: 07 4391 2574 Fax: 07 43916420
reception@ferncrestlodgeyarrondi.example
www.ferncrestlodgeyarrondi.example
like us on Chatterleaf

```html
<!DOCTYPE html>
<html lang="en">
<head>
<meta charset="utf-8">
<title>Ferncrest Lodge Yarrondi – Business Card</title>
<link href="https://fonts.googleapis.com/css2?family=Lato:wght@400;700&display=swap" rel="stylesheet">
<style>
  :root {
    --backdrop: #6e6e6e;
    --card: #ffffff;
    --brand-blue: #2f56a6;
    --brand-green: #8dc63f;
    --text-light: #ffffff;
    --badge-border: #c9cfdc;
  }
  * { box-sizing: border-box; margin: 0; padding: 0; }
  html, body {
    width: 1200px; height: 900px; overflow: hidden;
    background: var(--backdrop);
    font-family: 'Lato', Arial, sans-serif;
  }
  .business-card {
    position: absolute; left: 100px; top: 160px;
    width: 1000px; height: 580px;
    background: var(--card);
    overflow: hidden;
  }
  .card-shapes { position: absolute; inset: 0; }
  .wordmark {
    position: absolute; left: 300px; top: 150px;
    display: flex; align-items: center; gap: 16px;
  }
  .wordmark-dot {
    width: 40px; height: 40px; border-radius: 50%;
    background: var(--brand-green);
  }
  .wordmark-name {
    font-weight: 700; font-size: 38px; color: var(--brand-blue);
  }
  .social-badge {
    position: absolute; right: 28px; top: 44px;
    display: flex; align-items: center; gap: 10px;
    padding: 8px 14px 8px 8px;
    border: 2px solid var(--badge-border); border-radius: 6px;
  }
  .social-square {
    width: 52px; height: 52px; background: var(--brand-blue); border-radius: 4px;
  }
  .social-text { color: var(--brand-blue); line-height: 1; }
  .social-invite { font-size: 13px; font-weight: 700; letter-spacing: 1px; }
  .social-name { font-size: 30px; font-weight: 700; margin-top: 4px; }
  .business-name {
    position: absolute; left: 48px; top: 434px;
    color: var(--text-light); white-space: nowrap;
  }
  .business-name h1 { font-size: 34px; font-weight: 700; }
  .business-name p { font-size: 20px; font-weight: 700; margin-top: 6px; }
  .contact-list {
    position: absolute; right: 40px; top: 340px;
    list-style: none; text-align: right; white-space: nowrap;
    color: var(--text-light); font-size: 19px; line-height: 40px;
  }
  .contact-list b { font-weight: 700; }
</style>
</head>
<body>
  <main class="business-card">
    <svg class="card-shapes" viewBox="0 0 1000 580" width="1000" height="580" aria-hidden="true">
      <path fill="var(--brand-green)" d="M0,423 L400,423 Q460,423 480,470 L500,516 L0,516 Z"/>
      <path fill="var(--brand-blue)" d="M0,516 L470,516 C520,516 530,400 600,365 C690,320 820,312 1000,312 L1000,580 L0,580 Z"/>
    </svg>

    <div class="wordmark">
      <span class="wordmark-dot"></span>
      <span class="wordmark-name">Ferncrest Lodge Yarrondi</span>
    </div>

    <div class="social-badge">
      <span class="social-square"></span>
      <div class="social-text">
        <div class="social-invite">LIKE US ON</div>
        <div class="social-name">Chatterleaf</div>
      </div>
    </div>

    <div class="business-name">
      <h1>Ferncrest Lodge Yarrondi</h1>
      <p>Licensed Café/ Restaurant &amp; Motel</p>
    </div>

    <ul class="contact-list">
      <li><b>fax:</b> 07 43916420</li>
      <li><b>phone:</b> 07 4391 2574</li>
      <li><b>email:</b> www.ferncrestlodgeyarrondi.example</li>
      <li><b>web:</b> reception@ferncrestlodgeyarrondi.example</li>
      <li><b>address:</b> 14 Coralwood Lane KELBRIDGE Qld 4823</li>
    </ul>
  </main>
</body>
</html>
```